Business Cards

I'd like help creating business cards with the full logo "Veltrona Capital Partners" on the back of the card (navy background with white writing), and abbreviated logo "VCP" on the front. Would like to list name, title, phone number, email, and website listed on front of card. Would like to keep very simple. Front font Arial or similar.

```html
<!DOCTYPE html>
<html lang="en">
<head>
<meta charset="utf-8">
<title>Veltrona Capital Partners – Business Cards</title>
<link href="https://fonts.googleapis.com/css2?family=Arimo:wght@400;700&family=Montserrat:wght@700&display=swap" rel="stylesheet">
<style>
  :root {
    --backdrop: #d6d6d6;
    --paper: #f1f1f0;
    --ink: #111111;
    --navy: #14206b;
    --navy-edge: #0d1650;
    --white: #ffffff;
  }
  html, body {
    margin: 0;
    padding: 0;
    width: 1200px;
    height: 1051px;
    overflow: hidden;
    background: var(--backdrop);
  }
  .canvas {
    position: relative;
    width: 1200px;
    height: 1051px;
  }
  .card {
    position: absolute;
    left: 320px;
    width: 560px;
    height: 320px;
    box-sizing: border-box;
    box-shadow: 0 14px 30px rgba(0,0,0,0.18);
  }
  .card-front {
    top: 170px;
    background: var(--paper);
    font-family: "Arimo", Arial, sans-serif;
    color: var(--ink);
    display: flex;
    align-items: center;
    padding: 0 40px 0 48px;
  }
  .monogram {
    display: flex;
    align-items: center;
    gap: 14px;
    width: 230px;
  }
  .monogram-square {
    width: 22px;
    height: 22px;
    background: var(--ink);
  }
  .monogram-name {
    font-weight: 700;
    font-size: 76px;
    letter-spacing: 1px;
    line-height: 1;
  }
  .divider {
    width: 1.5px;
    height: 170px;
    background: var(--ink);
    margin: 0 26px 0 10px;
  }
  .contact { font-size: 15px; line-height: 1.35; }
  .contact-name {
    font-weight: 700;
    font-size: 19px;
    text-transform: uppercase;
    margin: 0;
  }
  .contact-title { margin: 0 0 8px; }
  .contact-address { margin: 0 0 8px; }
  .contact-list { list-style: none; margin: 0; padding: 0; }
  .contact-list li { display: flex; align-items: center; gap: 7px; }
  .contact-list svg { width: 12px; height: 12px; flex: none; }

  .card-back {
    top: 560px;
    background: var(--navy);
    border-bottom: 6px solid var(--navy-edge);
    display: flex;
    flex-direction: column;
    align-items: center;
    justify-content: center;
    font-family: "Montserrat", sans-serif;
    font-weight: 700;
    color: var(--white);
    text-transform: uppercase;
  }
  .brand-name { font-size: 62px; letter-spacing: 3px; line-height: 1; }
  .brand-sub { font-size: 24px; letter-spacing: 12px; margin-top: 14px; }
</style>
</head>
<body>
<main class="canvas">
  <section class="card card-front" aria-label="Business card front">
    <div class="monogram">
      <span class="monogram-square"></span>
      <span class="monogram-name">VCP</span>
    </div>
    <div class="divider"></div>
    <div class="contact">
      <p class="contact-name">Daniel Marsh</p>
      <p class="contact-title">Managing Director</p>
      <p class="contact-address">Your address, City<br>State, Zip 1234</p>
      <ul class="contact-list">
        <li>
          <svg viewBox="0 0 24 24" aria-hidden="true"><path fill="currentColor" d="M6.6 10.8a15 15 0 0 0 6.6 6.6l2.2-2.2a1 1 0 0 1 1-.25 11 11 0 0 0 3.6.6 1 1 0 0 1 1 1V20a1 1 0 0 1-1 1A17 17 0 0 1 3 4a1 1 0 0 1 1-1h3.5a1 1 0 0 1 1 1 11 11 0 0 0 .6 3.6 1 1 0 0 1-.25 1z"/></svg>
          123 456 789
        </li>
        <li>
          <svg viewBox="0 0 24 24" aria-hidden="true"><path fill="currentColor" d="M2 5h20v14H2zm2 2v.5l8 5 8-5V7zm0 2.8V17h16V9.8l-8 5z"/></svg>
          info@veltronamail.com
        </li>
        <li>
          <svg viewBox="0 0 24 24" aria-hidden="true"><circle cx="12" cy="12" r="9.5" fill="none" stroke="currentColor" stroke-width="2"/><path d="M2.5 12h19M12 2.5c3 3 3 16 0 19M12 2.5c-3 3-3 16 0 19" fill="none" stroke="currentColor" stroke-width="1.6"/></svg>
          www.veltronacapital.com
        </li>
      </ul>
    </div>
  </section>

  <section class="card card-back" aria-label="Business card back">
    <span class="brand-name">Veltrona</span>
    <span class="brand-sub">Capital Partners</span>
  </section>
</main>
</body>
</html>
```